Fresh web design for high profile Golf Club

We need an exciting web site that serves both members and visitors. Our current site has the relevant sections and pages but lacks a visual impact. There are a number of very good looking golf websites out there and we want to look the best.
We need a site that will attract golfers from all over Australia to come to our course to enjoy one of the finest 36 hole championship courses as well as fantastic clubhouse facilities on their next golfing holiday.
The member section needs to provide relevant information pages and regular news and event updates to 3000 members. We are situated on the Murray River with over 300 days of sunshine and ideal golfing weather every year.
We would like to stay with our existing logo and colours as a theme.

Target Market(s)

Golfers looking for golf holiday packages.

Industry/Entity Type

Club

Requirements
Must have
• Must have contact number for golf package holidays. Must have button for member entry and button for visitor entry. Existing site is www.kelvaronegolf.com.au. Looking for a big improvement in the look of the home page.
Nice to have
• Would like constantly updated weather reporting from source such as weather channel.

```html
<!DOCTYPE html>
<html lang="en">
<head>
<meta charset="utf-8">
<title>Kelvarone Golf Club</title>
<link href="https://fonts.googleapis.com/css2?family=Questrial&family=PT+Sans:ital,wght@0,400;0,700;1,400;1,700&family=Marcellus&family=Didact+Gothic&family=Oswald:wght@500;700&family=Alfa+Slab+One&display=swap" rel="stylesheet">
<style>
:root{
  --teal:#3fa5b8;
  --teal-dark:#2a8fa6;
  --green:#6fb52c;
  --green-dark:#4e8f17;
  --ink:#333333;
  --grey:#6b6b6b;
  --line:#d9d9d9;
  --page:#f2f2f2;
  --footer:#4a4a4a;
  --blue:#1b7fc4;
  --red:#c0282d;
  --purple:#9b19c9;
  --ad-blue:#1e9fe6;
  --lilac:#a96ee8;
}
*{box-sizing:border-box;margin:0;padding:0}
html,body{width:1108px;height:1200px;overflow:hidden}
body{position:relative;background:var(--page);font-family:"PT Sans",sans-serif;color:var(--ink)}

/* header */
.header{position:absolute;left:0;top:0;width:1108px;height:125px;background:#fff}
.brand{position:absolute;left:94px;top:34px;display:flex;align-items:center;gap:12px}
.brand-dot{width:34px;height:34px;border-radius:50%;background:var(--teal)}
.brand-name{font-family:"Questrial",sans-serif;font-size:26px;letter-spacing:5px;color:#4a4a4a;text-transform:uppercase}
.top-links{position:absolute;right:98px;top:5px;font-size:11.5px;color:#444;display:flex;align-items:center;gap:8px}
.top-links .sep{color:#999}
.phone{position:absolute;left:746px;top:52px;display:flex;align-items:center;gap:6px}
.phone-icon{width:42px;height:42px;border-radius:50%;background:radial-gradient(circle at 35% 30%,#5ab4f0,#1565b0)}
.phone-num{font-family:"Questrial",sans-serif;font-size:33px;color:#3b3b3b}

/* nav */
.nav{position:absolute;left:94px;top:121px;width:920px;height:37px;display:flex;background:linear-gradient(#fff,#ececec);box-shadow:0 1px 3px rgba(0,0,0,.25);z-index:3}
.nav a{display:flex;align-items:center;justify-content:center;font-size:12px;color:#333;text-decoration:none;border-right:1px solid #d6d6d6}
.nav a.active{background:var(--teal);color:#fff}

/* hero */
.hero{position:absolute;left:0;top:125px;width:1104px;height:420px;background:linear-gradient(180deg,#8fb8c6 0%,#6f9a58 22%,#8db556 45%,#d9d2c0 70%,#e6ded0 100%)}
.arrow{position:absolute;top:305px}
.hero-box{position:absolute;left:587px;top:175px;width:381px;height:278px;background:rgba(55,55,55,.75);border:1px solid rgba(255,255,255,.55)}
.hero-title{position:absolute;left:18px;top:8px;font-family:"Didact Gothic",sans-serif;font-size:27px;color:#f2d41a;line-height:1}
.hero-title .big{display:block;font-family:"PT Sans",sans-serif;font-style:italic;font-weight:700;font-size:30px;letter-spacing:3px;color:#7fc7d8;margin-top:4px}
.hero-text{position:absolute;left:20px;top:94px;width:344px;font-size:12.6px;line-height:16.6px;color:#fff;text-align:justify}
.hero-text b{font-style:italic}
.quote-btn{position:absolute;left:17px;top:240px;width:180px;height:40px;border-radius:12px;background:linear-gradient(#8fd14a,var(--green-dark));border:2px solid #c9ea9c;color:#fff;font-weight:700;font-size:17px;display:flex;align-items:center;justify-content:center}
.ball-art{position:absolute;left:280px;top:190px;width:90px;height:82px;border-radius:10px;background:linear-gradient(#e9e9e9,#4b9a2a)}

/* main panel */
.panel{position:absolute;left:97px;top:489px;width:919px;height:605px;background:#fff;border-radius:18px;box-shadow:0 0 4px rgba(0,0,0,.08)}
.welcome{position:absolute;left:25px;top:16px;display:flex;gap:8px}
.welcome-dot{width:42px;height:42px;border-radius:50%;background:radial-gradient(circle,#f4d21b 0 30%,var(--teal) 31% 65%,var(--green) 66%)}
.welcome h1{font-family:"Didact Gothic",sans-serif;font-weight:400;font-size:23px;line-height:24px;color:#222}
.welcome h1 span{display:block;font-family:"PT Sans",sans-serif;font-style:italic;font-weight:700;color:var(--teal);letter-spacing:1px}
.intro{position:absolute;left:27px;top:70px;width:624px;font-size:11.6px;line-height:16.6px;font-style:italic;font-weight:700;color:var(--green)}
.body-copy{position:absolute;left:27px;top:120px;width:624px;font-size:11.3px;line-height:16.6px;color:#333;text-align:justify}
.body-copy p{margin-bottom:16.6px}
.watch{position:absolute;left:24px;top:268px;font-family:"Marcellus",serif;font-size:24px;color:var(--teal-dark);display:flex;align-items:center;gap:8px}
.pdf{position:absolute;width:296px;height:94px;background:linear-gradient(135deg,#fff 60%,#ececec);box-shadow:0 3px 6px rgba(0,0,0,.08)}
.pdf-icon{position:absolute;left:12px;top:22px;width:48px;height:56px;border-radius:3px;background:linear-gradient(#fff,#ddd);border:1px solid #ccc}
.pdf-icon::after{content:"";position:absolute;left:9px;top:12px;width:28px;height:28px;background:var(--red);border-radius:3px}
.pdf-text{position:absolute;left:80px;top:18px;font-size:11.6px;line-height:17px;color:#222}
.pdf-text b{color:var(--red)}

.ad-cup{position:absolute;left:47px;top:452px;width:265px;height:122px;background:#fff;border:1px solid #ddd;overflow:hidden}
.ad-cup .bar{height:36px;background:var(--lilac);color:#fff;font-family:"Oswald",sans-serif;font-weight:700;font-size:24px;text-align:center;line-height:36px}
.ad-cup .gala{font-family:"Oswald",sans-serif;font-size:21px;color:#e0248a;padding:2px 7px 0;line-height:24px}
.ad-cup .gala small{font-size:14px}
.ad-cup .tix{font-family:"Oswald",sans-serif;font-size:14px;color:#1a9a2e;padding:0 7px;line-height:18px}
.ad-cup .mc{margin:6px auto 0;width:180px;height:28px;border-radius:14px;background:var(--lilac);color:#fff;font-family:"Oswald",sans-serif;font-size:18px;text-align:center;line-height:28px}

.ad-rate{position:absolute;left:346px;top:452px;width:276px;height:122px;background:var(--ad-blue);border:2px solid #f1d32a;color:#fff;font-weight:700;overflow:hidden}
.ad-rate .name{position:absolute;left:8px;top:10px;font-family:"Questrial",sans-serif;font-size:13px;letter-spacing:2px;font-weight:400}
.ad-rate .fees{position:absolute;left:20px;top:48px;font-size:9px;line-height:10.6px}
.ad-rate .fees td{padding-right:14px}
.ad-rate .fine{position:absolute;left:6px;top:106px;font-size:5.5px;font-weight:400;line-height:6px}
.ad-rate .side{position:absolute;left:140px;top:0;width:134px;height:118px;background:#fff;color:var(--ad-blue);padding:6px 4px}
.ad-rate .side h3{font-family:"Oswald",sans-serif;font-weight:500;font-size:17px;line-height:18px;text-align:center}
.ad-rate .side .period{font-size:7.5px;text-align:center;line-height:9px;margin-top:4px}
.ad-rate .side .holes{font-size:8.5px;line-height:10px;margin-top:12px;width:60px;text-align:center}

/* members sidebar */
.divider{position:absolute;left:670px;top:30px;height:560px;border-left:1px dashed #bbb}
.members-icon{position:absolute;left:680px;top:21px;width:58px;height:58px;border-radius:8px;background:linear-gradient(135deg,#d8e9f4,#2f7fbf)}
.members-head{position:absolute;left:743px;top:22px;white-space:nowrap;font-family:"Oswald",sans-serif;font-weight:500;font-size:22px;line-height:28px;color:var(--teal-dark);letter-spacing:.5px}
.members-head span{color:var(--green)}
.members-sub{position:absolute;left:748px;top:53px;white-space:nowrap;font-family:"Didact Gothic",sans-serif;font-size:12.5px;line-height:14px;letter-spacing:2.6px;color:#666}
.testimonial{position:absolute;left:687px;width:220px}
.testimonial .mark{position:absolute;left:0;top:-6px;font-family:Georgia,serif;font-size:26px;color:#aaa}
.testimonial p{margin-left:21px;font-family:"PT Sans",sans-serif;font-size:11px;line-height:15px;color:#333;letter-spacing:.3px}
.testimonial .meta{margin:5px 0 0 21px;display:flex;justify-content:space-between;font-weight:700;font-size:11.5px;line-height:14px;color:var(--blue)}
.ad-show{position:absolute;left:704px;top:336px;width:199px;height:252px;background:var(--purple);border:2px solid #6a0f8c;padding:7px}
.ad-show .inner{width:100%;height:100%;border:2px solid #fff;text-align:center;color:#fff}
.ad-show .acts{font-family:"Alfa Slab One",serif;font-size:23px;line-height:32px;padding-top:4px}
.ad-show .acts small{font-size:13px}
.ad-show .tag{font-weight:700;font-size:12px;line-height:13px;margin-top:6px}
.ad-show .free{font-weight:700;font-size:15px;line-height:16px;color:#ffe3ff;margin-top:4px}
.ad-show .free span{display:block;color:#1a1a1a;background:#fff}
.ad-show .meals{background:#fff;color:var(--purple);font-weight:700;font-size:11.5px;line-height:13px;margin-top:4px;padding:2px 0}

/* footer */
.footer{position:absolute;left:0;top:1052px;width:1108px;height:148px;background:var(--footer);z-index:-1}
.footer-brand{position:absolute;left:97px;top:1122px;display:flex;align-items:center;gap:12px}
.footer-brand .brand-dot{background:#bdbdbd}
.footer-brand .brand-name{color:#bdbdbd}
.footer-info{position:absolute;right:99px;top:1106px;text-align:right;font-size:11.5px;line-height:16.7px;color:#fff;font-style:normal}
</style>
</head>
<body>

<header class="header">
  <div class="brand"><span class="brand-dot"></span><span class="brand-name">Kelvarone Golf Club</span></div>
  <div class="top-links">
    <svg width="11" height="14" viewBox="0 0 11 14"><rect x="1" y="6" width="9" height="8" rx="1" fill="#6fb52c"/><path d="M3 6V4a2.5 2.5 0 0 1 5 0v2" fill="none" stroke="#6fb52c" stroke-width="1.6"/></svg>
    <span>Members Login</span><span class="sep">|</span><span>Join Now</span>
  </div>
  <div class="phone">
    <span class="phone-icon">
      <svg width="42" height="42" viewBox="0 0 42 42"><path d="M15 12c-2 1-3 3-2 6 2 6 6 10 12 12 3 1 5 0 6-2l-4-4-3 2c-3-1-6-4-7-7l2-3z" fill="#fff"/></svg>
    </span>
    <span class="phone-num">020 5550 1234</span>
  </div>
</header>

<nav class="nav">
  <a class="active" style="width:67px">HOME</a>
  <a style="width:115px">MEMBERSHIP</a>
  <a style="width:74px">GOLF</a>
  <a style="width:111px">CLUB HOUSE</a>
  <a style="width:124px">NEWS &amp; EVENTS</a>
  <a style="width:128px">GOLF PACKAGES</a>
  <a style="width:104px">KELVARONE</a>
  <a style="width:92px">GALLERY</a>
  <a style="width:105px;border-right:0">CONTACT US</a>
</nav>

<section class="hero" role="img" aria-label="Photo of a golfer playing out of a sand bunker on a riverside course while another golfer watches"></section>
<svg class="arrow" style="left:112px" width="30" height="44" viewBox="0 0 30 44"><path d="M24 4 8 22l16 18" fill="none" stroke="#fff" stroke-width="7" stroke-linecap="round"/></svg>
<svg class="arrow" style="left:980px" width="30" height="44" viewBox="0 0 30 44"><path d="M6 4l16 18L6 40" fill="none" stroke="#fff" stroke-width="7" stroke-linecap="round"/></svg>

<div class="hero-box">
  <div class="hero-title">“A great golf course is just the<span class="big">BEGINNING ”</span></div>
  <p class="hero-text"><b>There's so much to do on the beautiful Murray River. Discover Kelvarone's 36 Hole</b> Championship Golf Course, glorious golden sandy beaches, Riverside SportAviation aerodrome, the Historic Air Museum, walking tracks, State Forests, National Parks and so much more. Experience the history.......</p>
  <div class="quote-btn">Request a Quote</div>
  <div class="ball-art" role="img" aria-label="Illustration of a golf ball on a tee with a club on a green block"></div>
</div>

<main class="panel">
  <div class="welcome">
    <span class="welcome-dot"></span>
    <h1>Welcome To<span>Kelvarone Golf Club</span></h1>
  </div>
  <p class="intro">The climate is better than Australia's famous Gold Coast with more than 300 days of sunshine, and mean temperatures of around 28°Celsius in January and 15°Celsius in July.</p>
  <div class="body-copy">
    <p>Kelvarone Golf Club invites you to experience this exceptional sporting venue situated on Australia's mighty Murray River. Home of the Southern Trainee Championships this is one of Australia's best presented 36 Hole Championship Golf Courses.</p>
    <p>If you're chasing that elusive Murray Cod, Waterskiing, Boating, Fishing, relaxing on a houseboat or sunbaking on our golden beaches, Kelvarone is the perfect place to base yourself for a Murray River break. We are central to all the Murray attractions as well as having over 350 golf holes within an hours drive. Social golfers are welcome here 7 days a week.</p>
    <p>A great golf course is just the beginning...</p>
  </div>
  <div class="watch">Watch Ned Calloway at the Kelvarone Golf Club
    <svg width="12" height="20" viewBox="0 0 12 20"><path d="M1 1l10 9-10 9z" fill="#6fb52c"/></svg>
  </div>

  <div class="pdf" style="left:9px;top:337px">
    <span class="pdf-icon"></span>
    <p class="pdf-text">To download a copy of the Kelvarone Golf<br>please click<br><b>2012 Annual Report (2).pdf</b></p>
  </div>
  <div class="pdf" style="left:321px;top:328px">
    <span class="pdf-icon"></span>
    <p class="pdf-text">To download a copy of the Kelvarone Golf<br>please click<br><b>2012 Annual Report (2).pdf</b></p>
  </div>

  <div class="ad-cup">
    <div class="bar">Spring Cup Calcutta</div>
    <div class="gala">Gala Night <small>Monday 5th Nov. 7pm</small></div>
    <div class="tix">$10 Calcutta Tickets on Sale NOW at Reception</div>
    <div class="mc">MC - Ned Calloway</div>
  </div>

  <div class="ad-rate">
    <span class="name">KELVARONE</span>
    <table class="fees">
      <tr><td>Full Golfing *</td><td>$175</td></tr>
      <tr><td>KGC Golf Pass *</td><td>$137.50</td></tr>
      <tr><td>Social</td><td>$15</td></tr>
      <tr><td>Junior</td><td>$25</td></tr>
    </table>
    <p class="fine">* Joining Fee $25 (applies to Full Golfing only)<br>* Conditions apply please see Application form</p>
    <div class="side">
      <h3>PRO-RATA<br>MEMBERSHIP</h3>
      <p class="period">Membership period:<br>1st October -<br>31st December 2012</p>
      <p class="holes">36 Championship Holes</p>
    </div>
  </div>

  <div class="divider"></div>
  <div class="members-icon" role="img" aria-label="Icon of a member seated at a desk"></div>
  <div class="members-head">Members <span>Say...</span></div>
  <div class="members-sub">Testimonial Area</div>

  <div class="testimonial" style="top:92px">
    <span class="mark">“</span>
    <p>The Board of the Kelvarone Golf Club has now finalised the purchase of High Security water......</p>
    <div class="meta"><span>Mr. Harrowby</span><span>more ▸ ▸</span></div>
  </div>
  <div class="testimonial" style="top:167px">
    <span class="mark">“</span>
    <p>The Board of the Kelvarone Golf Club has now finalised the purchase of High Security water......</p>
    <div class="meta"><span>Mr. Harrowby</span><span>more ▸ ▸</span></div>
  </div>
  <div class="testimonial" style="top:244px">
    <span class="mark">“</span>
    <p>The Board of the Kelvarone Golf Club has now finalised the purchase of High Security water......</p>
    <div class="meta"><span>Mr. Harrowby</span><span>more ▸ ▸</span></div>
  </div>

  <div class="ad-show">
    <div class="inner">
      <div class="acts">Jack Dalby <small>&amp;</small><br>Rory Kestrel</div>
      <div class="tag">Rock 'n' Roll Legends<br>Tribute Show</div>
      <div class="free">Free to See<span>Saturday 1st December</span></div>
      <div class="meals">Main meals from $9.90ea.<br>Come for dinner and<br>stay for a great night!</div>
    </div>
  </div>
</main>

<footer class="footer"></footer>
<div class="footer-brand"><span class="brand-dot"></span><span class="brand-name">Kelvarone Golf Club</span></div>
<address class="footer-info">
  Kelvarone Golf Club<br>
  Riverbend Rd, Kelvarone N.S.W. 2799<br>
  1800 555 019<br>
  Copyright © Kelvarone Golf Club 2011<br>
  Powered By: webfernstudio.com
</address>

</body>
</html>
```